Specialised investor in e-mobility and energy wants business card design

We need a business card design that fits our existing corporate design. <The look and feel must be 'sharp'/'clean', dynamic, communicate momentum, professionalism etc (as one would imagine from a firm in the financial sector). We like the idea of a reverse-side of the card that includes the logo, and the name and contact details on the other. We expect the deliverable to be whatever format might be required to be able to get cards printed directly by a service such as tandor press. Our website is www.orm.capital

```html
<!DOCTYPE html>
<html lang="en">
<head>
<meta charset="utf-8">
<title>ORM Capital – Business Card</title>
<link href="https://fonts.googleapis.com/css2?family=Montserrat:wght@400;500;700&display=swap" rel="stylesheet">
<style>
  :root {
    --bg: #ececec;
    --brand-green: #88b34c;
    --brand-dark: #2f4f1f;
    --ink: #1e1e1e;
    --paper: #ffffff;
    --card-w: 600px;
    --card-h: 343px;
  }
  * { margin: 0; padding: 0; box-sizing: border-box; }
  html, body {
    width: 1200px; height: 900px; overflow: hidden;
    background: var(--bg);
    font-family: "Montserrat", sans-serif;
  }
  .sheet {
    width: 1200px; height: 900px;
    display: flex; flex-direction: column;
    align-items: center; justify-content: center; gap: 40px;
  }
  .card {
    position: relative;
    width: var(--card-w); height: var(--card-h);
    overflow: hidden;
    box-shadow: 0 6px 18px rgba(0,0,0,0.12);
  }

  /* Logo side */
  .card--front { background: var(--brand-green); }
  .card--front .wordmark {
    position: absolute; inset: 0;
    display: flex; align-items: center; justify-content: center; gap: 16px;
  }
  .wordmark__dot {
    width: 22px; height: 22px; border-radius: 50%;
    background: var(--brand-dark);
  }
  .wordmark__name {
    font-weight: 500; font-size: 64px; letter-spacing: 0.5px;
    color: var(--brand-dark);
  }

  /* Details side */
  .card--back { background: var(--paper); }
  .card--back .wordmark {
    position: absolute; top: 34px; right: 36px;
    display: flex; align-items: center; gap: 10px;
  }
  .card--back .wordmark__dot { width: 12px; height: 12px; }
  .card--back .wordmark__name { font-size: 36px; }

  .person { position: absolute; top: 118px; left: 40px; }
  .person__name {
    font-weight: 700; font-size: 17px; letter-spacing: 0.6px;
    color: var(--brand-green); text-transform: uppercase;
  }
  .person__role { font-size: 15px; color: var(--ink); margin-top: 2px; }

  .company {
    position: absolute; top: 158px; right: 36px;
    text-align: right; font-size: 15px; line-height: 1.35; color: var(--ink);
  }

  .contact {
    position: absolute; left: 40px; bottom: 62px;
    list-style: none; font-size: 16px; color: var(--ink); line-height: 1.45;
  }
  .contact li { display: flex; align-items: center; gap: 9px; }
  .contact svg { width: 14px; height: 14px; fill: var(--brand-green); }

  .footer-bands { position: absolute; left: 0; bottom: 0; width: 600px; height: 64px; }
  .website {
    position: absolute; right: 30px; bottom: 22px;
    font-size: 16px; color: var(--paper); letter-spacing: 0.3px;
  }
</style>
</head>
<body>
<main class="sheet">
  <section class="card card--front" aria-label="Card front">
    <div class="wordmark">
      <span class="wordmark__dot"></span>
      <span class="wordmark__name">ORM capital</span>
    </div>
  </section>

  <section class="card card--back" aria-label="Card back">
    <div class="wordmark">
      <span class="wordmark__dot"></span>
      <span class="wordmark__name">ORM capital</span>
    </div>

    <div class="person">
      <p class="person__name">Peter Hallworth</p>
      <p class="person__role">team directly</p>
    </div>

    <div class="company">
      <p>ORM Capital S.A.</p>
      <p>Geneva, Switzerland</p>
    </div>

    <ul class="contact">
      <li>
        <svg viewBox="0 0 16 16" aria-hidden="true"><path d="M3 1h3l1.5 4-2 1.3a9 9 0 0 0 4.2 4.2L11 8.5l4 1.5v3a2 2 0 0 1-2 2A12 12 0 0 1 1 3a2 2 0 0 1 2-2z"/></svg>
        <span>+41 79555 0148</span>
      </li>
      <li>
        <svg viewBox="0 0 16 16" aria-hidden="true"><path d="M1 3h14v10H1z M1.5 3.5 8 9l6.5-5.5" fill="var(--brand-green)"/><path d="M1.5 3.8 8 9.2l6.5-5.4" fill="none" stroke="#fff" stroke-width="1.2"/></svg>
        <span>peter@orm.capital</span>
      </li>
    </ul>

    <svg class="footer-bands" viewBox="0 0 600 64" aria-hidden="true">
      <rect x="0" y="34" width="398" height="3" fill="var(--brand-green)"/>
      <rect x="0" y="44" width="398" height="20" fill="var(--brand-dark)"/>
      <polygon points="410,6 600,6 600,64 404,64" fill="var(--brand-green)"/>
    </svg>
    <p class="website">www.orm.capital</p>
  </section>
</main>
</body>
</html>
```